Seaside commercial building needs a design for a prominent sign

we have bought a small commercial building in a small seaside area. The building was in disrepair and we are rebuilding it and will rent to small businesses. We have a tall sign right on the corner of the area and want to design something special for the sign The address is 2738 and we want to incorporate that into the name, or just have that as the name. The area is called Bonnet Shores which we were going to use and call it Marlow Corner. Almost all shops, however use Bonnet in their name. Looking for something unique with a sea-related logo. Elegant, yet welcoming.

```html
<!DOCTYPE html>
<html lang="en">
<head>
<meta charset="utf-8">
<title>2738 Marlow Corner – Corner Sign</title>
<link rel="stylesheet" href="https://fonts.googleapis.com/css2?family=Arimo:wght@400;700&family=Cinzel:wght@700&display=swap">
<style>
  :root {
    --sea: #68d5da;
    --sea-deep: #5ccfd5;
    --sea-pale: #d6f4f5;
    --paper: #ffffff;
  }
  html, body {
    margin: 0;
    padding: 0;
    width: 815px;
    height: 1200px;
    overflow: hidden;
    background: var(--paper);
  }
  .sign {
    display: block;
    width: 815px;
    height: 1200px;
  }
  .frame {
    fill: none;
    stroke: var(--sea);
    stroke-width: 8;
    stroke-linejoin: round;
  }
  .slat {
    stroke: var(--sea);
    stroke-width: 8;
  }
  .address-number {
    font-family: "Arimo", Arial, sans-serif;
    font-weight: 400;
    font-size: 87px;
    fill: var(--sea);
  }
  .building-name {
    font-family: "Cinzel", Georgia, serif;
    font-weight: 700;
    font-size: 42px;
    fill: var(--sea);
  }
  .panel-label {
    font-family: "Arimo", Arial, sans-serif;
    font-weight: 700;
    font-size: 42px;
    letter-spacing: 1px;
    fill: var(--sea);
  }
</style>
</head>
<body>
<svg class="sign" viewBox="0 0 815 1200" xmlns="http://www.w3.org/2000/svg">
  <defs>
    <linearGradient id="sea-band" x1="0" y1="0" x2="0" y2="1">
      <stop offset="0" stop-color="var(--sea-deep)"/>
      <stop offset="1" stop-color="var(--sea-pale)"/>
    </linearGradient>
  </defs>

  <!-- posts -->
  <g class="posts">
    <rect class="frame" x="133" y="164" width="41" height="923" rx="9"/>
    <rect class="frame" x="119" y="100" width="67" height="64" rx="14"/>
    <rect class="frame" x="650" y="164" width="41" height="923" rx="9"/>
    <rect class="frame" x="637" y="100" width="68" height="64" rx="14"/>
  </g>

  <!-- arched sign body -->
  <path class="frame" d="M174 1000 V252 C174 160 280 100 410 100 C540 100 646 160 646 252 V1000"/>

  <!-- address oval -->
  <ellipse class="frame" cx="412" cy="203" rx="137" ry="71"/>
  <text class="address-number" x="412" y="234" text-anchor="middle">2738</text>

  <text class="building-name" x="414" y="330" text-anchor="middle" textLength="398" lengthAdjust="spacingAndGlyphs">MARLOW CORNER</text>

  <!-- sea ornament area -->
  <rect role="img" aria-label="Sea wave ornament" x="178" y="336" width="464" height="66" fill="url(#sea-band)"/>

  <!-- slats -->
  <g class="slats">
    <line class="slat" x1="174" y1="430" x2="646" y2="430"/>
    <line class="slat" x1="174" y1="508" x2="646" y2="508"/>
    <line class="slat" x1="174" y1="610" x2="646" y2="610"/>
    <line class="slat" x1="174" y1="711" x2="646" y2="711"/>
    <line class="slat" x1="174" y1="813" x2="646" y2="813"/>
    <line class="slat" x1="174" y1="899" x2="646" y2="899"/>
    <line class="slat" x1="174" y1="1000" x2="646" y2="1000"/>
  </g>

  <!-- panel labels -->
  <text class="panel-label" x="412" y="578" text-anchor="middle">PROPERTIES</text>
  <text class="panel-label" x="412" y="781" text-anchor="middle">BALCONY</text>
  <text class="panel-label" x="412" y="969" text-anchor="middle">FOR LEASE</text>
</svg>
</body>
</html>
```